Meridale Vantage Alliance Web Design

I would like a web design for a conference. Registration, Form completion, Hotel, Speakers etc. See link for sample similar but not the same.
http://qrvlo.example/pldwk/index.php/contact-us
We would like the design to depict the colours of the logo which is attached. A banner of the website will be provided. We would like a transitioning space in the top and front page of the website for announcements and showcase of events. We would like custom prepared headers for each grouping, example, Sponsor, Venue, Discussion etc.

Hotel

Coded - Design and coding required

```html
<!DOCTYPE html>
<html lang="en">
<head>
<meta charset="utf-8">
<title>Meridale Vantage Alliance Conference</title>
<link href="https://fonts.googleapis.com/css2?family=Raleway:wght@400;600;800&family=Open+Sans:wght@400;600&family=Roboto+Condensed:wght@400&display=swap" rel="stylesheet">
<style>
:root{
  --page-bg-1:#cfd6f2;
  --page-bg-2:#b9c2ec;
  --white:#ffffff;
  --nav-blue:#1f66c1;
  --nav-blue-dark:#1857a8;
  --footer-blue:#1d5fb8;
  --red:#e2262b;
  --orange:#ec7b12;
  --feature-orange:#ea9412;
  --feature-teal:#22a596;
  --feature-green:#78bf30;
  --ink:#222;
  --body:#444;
  --link-blue:#1a4f9c;
  --light-grey:#f2f2f2;
  --rule:#e2e2e2;
}
*{box-sizing:border-box;margin:0;padding:0}
html,body{width:749px;height:1200px;overflow:hidden}
body{
  position:relative;
  font-family:"Open Sans",sans-serif;
  color:var(--body);
  background:linear-gradient(160deg,var(--page-bg-1) 0%,#dfe3f6 40%,var(--page-bg-2) 100%);
}
.page{position:absolute;left:62px;top:22px;width:626px}
.site-header{position:relative;height:93px;background:var(--white)}
.brand{position:absolute;left:18px;top:28px;display:flex;align-items:center;gap:8px}
.brand-mark{width:26px;height:26px;border-radius:50%;background:var(--nav-blue)}
.brand-name{font-family:"Open Sans",sans-serif;font-weight:600;font-size:11px;line-height:13px;color:var(--ink);width:120px}
.call{position:absolute;left:340px;top:36px;display:flex;gap:8px}
.call-icon{width:26px;height:26px;border:1.5px solid var(--red);border-radius:50%;display:flex;align-items:center;justify-content:center}
.call-label{font-size:10.5px;color:var(--ink);line-height:13px}
.call-number{font-size:13px;color:var(--red);line-height:16px}
.search{position:absolute;left:492px;top:33px;width:118px;height:24px;border:1px solid #e4e4e4;display:flex;align-items:center;justify-content:space-between;padding:0 7px 0 9px;font-size:7.5px;color:#555}
.main-nav{position:relative;height:36px;background:var(--nav-blue);font-family:"Roboto Condensed",sans-serif;font-size:11px;color:var(--white)}
.main-nav span{position:absolute;top:11px}
.main-nav .current{left:0;top:0;width:58px;height:36px;background:var(--nav-blue-dark);display:flex;align-items:center;justify-content:center}
.hero{position:relative;height:313px;overflow:hidden}
.hero-photo{position:absolute;inset:0;background:linear-gradient(180deg,#a99884 0%,#c8bba9 45%,#8a6f63 80%,#5c4a44 100%)}
.hero-title{position:absolute;left:67px;top:97px;font-family:"Raleway",sans-serif;font-weight:800;font-size:30px;color:var(--white);letter-spacing:.5px}
.hero-sub{position:absolute;left:67px;top:134px;font-family:"Raleway",sans-serif;font-weight:800;font-size:19px;color:var(--white)}
.hero-cta{position:absolute;left:68px;top:162px;width:126px;height:29px;background:var(--orange);color:var(--white);font-family:"Roboto Condensed",sans-serif;font-size:11px;display:flex;align-items:center;justify-content:center;gap:6px}
.hero-arrow{position:absolute;top:147px;width:22px;height:22px;border-radius:50%;background:rgba(70,60,55,.6);display:flex;align-items:center;justify-content:center}
.welcome{position:relative;height:244px;background:var(--white);border-top:3px solid #eee}
.section-title{font-family:"Raleway",sans-serif;font-weight:400;color:var(--ink)}
.welcome .section-title{position:absolute;left:17px;top:22px;font-size:19px}
.welcome-photo{position:absolute;left:17px;top:65px;width:162px;height:143px;background:linear-gradient(135deg,#2b3a5c,#b4473a 60%,#d8b7a0)}
.welcome-copy{position:absolute;left:194px;top:62px;width:226px;font-size:7.2px;line-height:12.8px;color:#333}
.welcome-copy p{margin-bottom:8px}
.read-more{display:block;margin-top:12px;font-family:"Raleway",sans-serif;font-size:8.5px;color:var(--ink)}
.sponsor{position:absolute;left:441px;top:56px;width:170px;height:152px;background:#f8f6f0;border:1px solid #e4e4e4}
.sponsor-head{height:29px;background:#efefef;font-family:"Raleway",sans-serif;font-size:13px;color:var(--ink);display:flex;align-items:center;justify-content:center}
.sponsor-name{position:absolute;left:0;right:0;top:80px;text-align:center;font-family:"Open Sans",sans-serif;font-weight:600;font-size:14px;color:var(--link-blue)}
.features{position:relative;height:216px;background:var(--light-grey);padding:24px 17px 0;display:flex;gap:16px}
.feature{width:187px;height:160px;color:var(--white);text-align:center;padding-top:19px}
.feature-orange{background:var(--feature-orange)}
.feature-teal{background:var(--feature-teal)}
.feature-green{background:var(--feature-green)}
.feature-icon{width:58px;height:58px;margin:0 auto;border:1.5px solid rgba(255,255,255,.85);border-radius:50%;display:flex;align-items:center;justify-content:center}
.feature h3{font-family:"Raleway",sans-serif;font-weight:400;font-size:17px;margin-top:9px}
.feature p{font-size:7.5px;font-weight:600;line-height:12px;padding:4px 12px 0}
.events{position:relative;height:176px;background:var(--white);border-top:3px solid #eee}
.events .section-title{position:absolute;left:16px;top:24px;font-size:15px}
.event{position:absolute;top:58px;display:flex;gap:13px}
.event-photo{width:93px;height:85px}
.event-a .event-photo{background:linear-gradient(135deg,#23324f,#b24c3f 60%,#c9a995)}
.event-b .event-photo{background:linear-gradient(135deg,#d9cfc6,#6f8eb5 60%,#3e4f72)}
.event h4{font-family:"Raleway",sans-serif;font-weight:600;font-size:9px;color:var(--link-blue)}
.event-time{font-family:"Raleway",sans-serif;font-size:7.5px;color:#333;margin-top:8px;display:flex;align-items:center;gap:4px}
.event p{font-family:"Raleway",sans-serif;font-size:7.5px;line-height:14px;color:#444;margin-top:5px;width:180px;padding-bottom:6px;border-bottom:1px solid var(--rule)}
.site-footer{position:absolute;left:0;top:1136px;width:749px;height:64px;background:var(--footer-blue);color:var(--white);font-size:7.5px}
.copyright{position:absolute;left:63px;top:23px}
.legal{position:absolute;left:62px;top:39px}
.social{position:absolute;left:586px;top:20px;display:flex;gap:5px}
.social span{width:16px;height:16px}
</style>
</head>
<body>
<div class="page">
  <header class="site-header">
    <div class="brand"><span class="brand-mark"></span><span class="brand-name">Meridale Vantage Alliance Conference 2015</span></div>
    <div class="call">
      <span class="call-icon"><svg width="12" height="12" viewBox="0 0 24 24"><path fill="#e2262b" d="M6.6 10.8a15 15 0 0 0 6.6 6.6l2.2-2.2c.3-.3.7-.4 1-.2 1.1.4 2.3.6 3.6.6.6 0 1 .4 1 1V20c0 .6-.4 1-1 1A17 17 0 0 1 3 4c0-.6.4-1 1-1h3.5c.6 0 1 .4 1 1 0 1.3.2 2.5.6 3.6.1.3 0 .7-.2 1z"/></svg></span>
      <div><div class="call-label">Speak to us today</div><div class="call-number">+1 555 0142-7730</div></div>
    </div>
    <div class="search">Search<svg width="9" height="9" viewBox="0 0 24 24"><circle cx="10" cy="10" r="7" fill="none" stroke="#333" stroke-width="3"/><path d="M15 15l7 7" stroke="#333" stroke-width="3"/></svg></div>
  </header>
  <nav class="main-nav">
    <span class="current">Home</span>
    <span style="left:76px">About Us</span>
    <span style="left:156px">Conference Info</span>
    <span style="left:259px">Programme</span>
    <span style="left:346px">Speakers</span>
    <span style="left:428px">Presentations</span>
    <span style="left:528px">Contact Us</span>
  </nav>
  <section class="hero">
    <div class="hero-photo" role="img" aria-label="Speaker with a microphone addressing a seated conference audience"></div>
    <h1 class="hero-title">MERIDALE VANTAGE</h1>
    <div class="hero-sub">Alliance Annual Conference</div>
    <div class="hero-cta"><svg width="9" height="9" viewBox="0 0 24 24"><path fill="#fff" d="M6.6 10.8a15 15 0 0 0 6.6 6.6l2.2-2.2c.3-.3.7-.4 1-.2 1.1.4 2.3.6 3.6.6.6 0 1 .4 1 1V20c0 .6-.4 1-1 1A17 17 0 0 1 3 4c0-.6.4-1 1-1h3.5c.6 0 1 .4 1 1 0 1.3.2 2.5.6 3.6.1.3 0 .7-.2 1z"/></svg>REQUEST A CALL BACK</div>
    <span class="hero-arrow" style="left:22px"><svg width="8" height="10" viewBox="0 0 8 10"><path d="M6 1L2 5l4 4" stroke="#fff" stroke-width="1.5" fill="none"/></svg></span>
    <span class="hero-arrow" style="left:578px"><svg width="8" height="10" viewBox="0 0 8 10"><path d="M2 1l4 4-4 4" stroke="#fff" stroke-width="1.5" fill="none"/></svg></span>
  </section>
  <section class="welcome">
    <h2 class="section-title">Welcome To Meridale Vantage</h2>
    <div class="welcome-photo" role="img" aria-label="Presenter at a laptop facing a large conference audience"></div>
    <div class="welcome-copy">
      <p>Lorem ipsum dolor sit amet, consectetur adipiscing elit, sed do eiusmod tempor incididunt ut labore et dolore magna aliqua. Ut enim ad minim veniam, quis nostrud exercitation ullamco laboris nisi ut aliquip ex ea commodo consequat. Duis aute irure dolor in reprehenderit in voluptate velit esse cillum dolore eu fugiat nulla pariatur. Excepteur sint occaecat cupidatat non proident.</p>
      <p>Lorem ipsum dolor sit amet, consectetur adipiscing elit, sed do eiusmod tempor incididunt ut labore et dolore magna aliqua. Ut enim ad minim veniam, quis nostrud exercitation</p>
      <span class="read-more">Read More +</span>
    </div>
    <aside class="sponsor">
      <div class="sponsor-head">Sponsor</div>
      <div class="sponsor-name">Solvane Fund</div>
    </aside>
  </section>
  <section class="features">
    <div class="feature feature-orange">
      <div class="feature-icon"><svg width="26" height="22" viewBox="0 0 26 22"><g fill="#fff"><circle cx="13" cy="6" r="4"/><circle cx="5" cy="7" r="3"/><circle cx="21" cy="7" r="3"/><path d="M6 20c0-5 3-8 7-8s7 3 7 8z"/><path d="M0 18c0-4 2-6 5-6 1 0 2 .3 2.5.8C6 14.5 5 17 5 18z"/><path d="M26 18c0-4-2-6-5-6-1 0-2 .3-2.5.8 1.5 1.7 2.5 4.2 2.5 5.2z"/></g></svg></div>
      <h3>Grouping</h3>
      <p>Aliquam posuere gravida tristique. Vestib dolor turpis, gravida vitae euismod at, consectetur quis felis. Etiam eget consectetur</p>
    </div>
    <div class="feature feature-teal">
      <div class="feature-icon"><svg width="16" height="24" viewBox="0 0 16 24"><path fill="#fff" d="M8 0a8 8 0 0 0-8 8c0 6 8 16 8 16s8-10 8-16a8 8 0 0 0-8-8zm0 11a3 3 0 1 1 0-6 3 3 0 0 1 0 6z"/></svg></div>
      <h3>Venue</h3>
      <p>Aliquam posuere gravida tristique. Vestib dolor turpis, gravida vitae euismod at, consectetur quis felis. Etiam eget consectetur</p>
    </div>
    <div class="feature feature-green">
      <div class="feature-icon"><svg width="28" height="22" viewBox="0 0 28 22"><g fill="none" stroke="#fff" stroke-width="2.2"><ellipse cx="11" cy="8" rx="9" ry="6"/><path d="M5 13l-2 5 6-3"/><path d="M21 9c3 1 5 3 5 5 0 1.5-1 3-3 4l1 3-4-2c-3 0-6-1-7-3"/></g></svg></div>
      <h3>Discussion</h3>
      <p>Aliquam posuere gravida tristique. Vestib dolor turpis, gravida vitae euismod at, consectetur quis felis. Etiam eget consectetur</p>
    </div>
  </section>
  <section class="events">
    <h2 class="section-title">Latest Events</h2>
    <article class="event event-a" style="left:17px">
      <div class="event-photo" role="img" aria-label="Presenter at a laptop in front of an audience"></div>
      <div>
        <h4>Nemo Enim Ipsam Voluptatem</h4>
        <div class="event-time"><svg width="7" height="7" viewBox="0 0 10 10"><circle cx="5" cy="5" r="4" fill="none" stroke="#333" stroke-width="1.5"/><path d="M5 3v2.3h2" stroke="#333" stroke-width="1.2" fill="none"/></svg>19.00 pm - 21.00 pm</div>
        <p>Vivamus elementum semper nisi. Lorem ipsum dolor sit amet, sectetuer adipiscing elit. Aenean commodo</p>
      </div>
    </article>
    <article class="event event-b" style="left:329px">
      <div class="event-photo" role="img" aria-label="Speaker holding a microphone"></div>
      <div>
        <h4>Nemo Enim Ipsam Voluptatem</h4>
        <div class="event-time"><svg width="7" height="7" viewBox="0 0 10 10"><circle cx="5" cy="5" r="4" fill="none" stroke="#333" stroke-width="1.5"/><path d="M5 3v2.3h2" stroke="#333" stroke-width="1.2" fill="none"/></svg>19.00 pm - 21.00 pm</div>
        <p>Vivamus elementum semper nisi. Lorem ipsum dolor sit amet, sectetuer adipiscing elit. Aenean commodo</p>
      </div>
    </article>
  </section>
</div>
<footer class="site-footer">
  <div class="copyright">Copyright © 2015 Meridale Vantage. All Rights Reserved.</div>
  <div class="legal">Terms &amp; Conditions &nbsp;/&nbsp; Privacy &amp; Disclaimer &nbsp;/&nbsp; Returns &amp; Refunds</div>
  <div class="social">
    <span style="background:#dd4b39"></span>
    <span style="background:#2d4f9b"></span>
    <span style="background:#1da1f2"></span>
    <span style="background:#1c6fb0"></span>
    <span style="background:#d8252b"></span>
  </div>
</footer>
</body>
</html>
```